Flyer-Design für Online-Schatzsuche
Zielgruppe
Der Name des Startups ist Lumora-Vex. Es handelt sich um eine Online-Schatzsuche. Irgendwo auf der Welt wird ein Schatz versteckt, der eine Million Euro wert ist. Die User registrieren sich für 19,99 Euro auf der Website und erhalten so den Zugang zu einer speziellen Seite(Quellzone), auf der wöchentlich neue Hinweise veröffentlicht werden, nachdem die Mindestanzahl an Teilnehmern (1Mio) erreicht ist. Diese Hinweise sind Rätsel aus den verschiedensten Bereichen, deren Lösungen GPS-Koordinaten und Aufenthaltsorte von weiteren Hinweisen oder dem Schatz selbst liefern.
Aufgabenstellung
Der Flyer sollte im DIN A6-Format gestaltet werden. Zudem soll er das Logo und die Domain www.lumora-vex.example enthalten. Außerdem soll der Flyer die Abenteuerlust anregen und sofort erkennbar machen, dass 1Mio Euro gewonnen werden können. Der Flyer soll später in Deutsch, Englisch, Japanisch und Mandarin vorliegen. Unter der 1Mio Euro sollte dann noch die umgerechnete Währung in amerikanischen Dollar, chinesischen Renminbi und Japanischen Yen stehen.

```html
<!DOCTYPE html>
<html lang="de">
<head>
<meta charset="utf-8">
<title>Lumora-Vex Flyer</title>
<link rel="stylesheet" href="https://fonts.googleapis.com/css2?family=Archivo+Black&family=Roboto+Condensed:wght@700&family=Arimo:wght@700&display=swap">
<style>
  :root {
    --fog-light: #c9cdcb;
    --fog-mid: #8d9290;
    --trunk-dark: #2c2e2d;
    --ground: #4a3f36;
    --moss: #55573f;
    --headline-light: rgba(205, 208, 206, 0.62);
    --headline-dark: rgba(40, 42, 41, 0.78);
    --brand-ink: #1e1f1e;
    --white: #ffffff;
    --url-grey: #d2d4d3;
  }
  html, body {
    margin: 0;
    padding: 0;
    overflow: hidden;
    background: #1a1b1a;
  }
  .flyer {
    position: relative;
    width: 851px;
    height: 1200px;
    overflow: hidden;
  }
  .forest-photo {
    position: absolute;
    inset: 0;
    background:
      linear-gradient(90deg, var(--trunk-dark) 0%, rgba(60,62,61,0.7) 18%, rgba(0,0,0,0) 40%, rgba(0,0,0,0) 70%, rgba(50,52,51,0.6) 100%),
      linear-gradient(180deg, var(--fog-mid) 0%, var(--fog-light) 35%, #9fa3a1 60%, var(--ground) 82%, var(--moss) 100%);
  }
  .brand {
    position: absolute;
    top: 24px;
    left: 392px;
    display: flex;
    align-items: center;
    gap: 16px;
  }
  .brand-name {
    font-family: "Arimo", sans-serif;
    font-weight: 700;
    font-size: 38px;
    color: var(--brand-ink);
    letter-spacing: 0.5px;
  }
  .brand-square {
    width: 76px;
    height: 76px;
    border: 3px solid var(--brand-ink);
    box-sizing: border-box;
  }
  .headline {
    position: absolute;
    top: 136px;
    left: 62px;
    margin: 0;
    font-family: "Archivo Black", sans-serif;
    font-weight: 400;
    font-size: 150px;
    line-height: 140px;
    letter-spacing: -5px;
    color: var(--headline-light);
    transform: scaleX(0.9);
    transform-origin: left top;
    white-space: nowrap;
  }
  .headline .dark { color: var(--headline-dark); }
  .prize-question {
    position: absolute;
    top: 604px;
    left: 70px;
    margin: 0;
    font-family: "Roboto Condensed", sans-serif;
    font-weight: 700;
    font-size: 54px;
    line-height: 1;
    color: var(--white);
    white-space: nowrap;
  }
  .prize-conversions {
    position: absolute;
    top: 668px;
    left: 72px;
    margin: 0;
    font-family: "Roboto Condensed", sans-serif;
    font-weight: 700;
    font-size: 22px;
    line-height: 1;
    color: var(--white);
    white-space: nowrap;
  }
  .website {
    position: absolute;
    top: 700px;
    left: 189px;
    margin: 0;
    font-family: "Arimo", sans-serif;
    font-weight: 700;
    font-size: 32px;
    color: var(--url-grey);
  }
</style>
</head>
<body>
  <main class="flyer">
    <div class="forest-photo" role="img" aria-label="Nebliger Buchenwald mit hohen dunklen Stämmen und laubbedecktem, moosigem Waldboden"></div>

    <div class="brand">
      <span class="brand-name">Lumora-Vex</span>
      <span class="brand-square"></span>
    </div>

    <h1 class="headline">Bist <span class="dark">du</span><br>ein <span class="dark">Aben-</span><br>teu<span class="dark">rer?</span></h1>

    <p class="prize-question">Hast du Lust auf 1 Million Euro?</p>
    <p class="prize-conversions">≈ 1,08 Mio. US-Dollar · 7,8 Mio. Renminbi · 160 Mio. Yen</p>

    <p class="website">www.lumora-vex.example</p>
  </main>
</body>
</html>
```